Re-design of an existing website

We are needing a redesign of http://www.corvane-pharmacy.com/. Same colour scheme and content. The design needs to be done using Zurb Foundation 5 with all SCSS included and setup accordingly.

Placeholder images may be used for now as photo's are in progress. Must be responsive and work on all device types.
Updates

PLEASE NOTE: The project manager is currently on holidays until the 6th of September, hopefully we will have a decision closer to this date but it may be a few days after.

Industry/Entity Type

Medical

Coding

Coded - Design and coding required

Number of Pages Required

3 page

Font styles to use
Sans Serif

Requirements
Must have
• Zurb Foundation 5

```html
<!DOCTYPE html>
<html lang="en">
<head>
<meta charset="utf-8">
<title>The Corvane Pharmacy</title>
<link rel="stylesheet" href="https://fonts.googleapis.com/css2?family=Open+Sans:wght@300;400;600;700&display=swap">
<style>
:root{
  --navy:#0d2f86;
  --navy-dark:#0a2570;
  --blue:#1f4fb3;
  --blue-light:#4f7fd6;
  --sky:#dbe7f6;
  --text:#555b66;
  --muted:#8a909a;
  --white:#ffffff;
  --line:#d7dce4;
  --footer:#0b2a78;
}
*{box-sizing:border-box;margin:0;padding:0}
html,body{width:1200px;height:2332px;overflow:hidden}
body{font-family:"Open Sans",Arial,sans-serif;color:var(--text);background:var(--white);position:relative}
.wrap{width:1040px;margin:0 auto;position:relative}

/* header */
.site-header{height:112px;background:var(--white)}
.site-header .wrap{height:112px;display:flex;align-items:center;justify-content:space-between}
.brand{display:flex;align-items:center;gap:14px}
.brand-mark{width:30px;height:30px;border-radius:50%;background:var(--navy)}
.brand-name{font-size:28px;font-weight:700;color:var(--navy);line-height:1.1}
.brand-tag{font-size:12px;color:var(--navy);font-weight:600;margin-top:2px}
.contact{font-size:13px;color:var(--text);display:flex;flex-direction:column;gap:10px}
.contact-row{display:flex;align-items:center;gap:10px}
.contact-icon{width:24px;height:24px;border-radius:50%;background:var(--navy);display:flex;align-items:center;justify-content:center}

/* nav */
.main-nav{height:28px;background:var(--navy)}
.main-nav ul{list-style:none;display:flex;height:28px;width:1040px;margin:0 auto}
.main-nav li{font-size:12px;color:var(--white);padding:0 14px;line-height:28px;white-space:nowrap}
.main-nav li.active{background:var(--blue-light)}

/* hero */
.hero{height:420px;position:relative;overflow:hidden}
.hero-photo{position:absolute;inset:0;background:linear-gradient(90deg,#c7d3df 0%,#e9eef3 40%,#f3ece6 60%,#d9e3ec 100%)}
.hero-caption{position:absolute;left:80px;top:100px;width:520px;background:rgba(255,255,255,.85);padding:22px 26px}
.hero-caption h1{font-size:40px;font-weight:400;color:var(--navy);line-height:1.1}
.hero-caption h1 strong{display:block;font-weight:400;letter-spacing:1px}
.hero-caption p{font-size:14px;color:var(--text);margin-top:12px;line-height:1.5}
.hero-dots{position:absolute;left:560px;bottom:18px;display:flex;gap:8px}
.hero-dots span{width:14px;height:14px;border:2px solid var(--white);background:rgba(255,255,255,.4)}
.hero-dots span.on{background:var(--white)}

/* intro */
.intro{height:340px;text-align:center;padding-top:56px}
.section-title{font-size:30px;font-weight:400;color:var(--navy)}
.rule{width:60px;height:2px;background:var(--blue);margin:14px auto 0}
.intro p{width:720px;margin:30px auto 0;font-size:13px;line-height:1.75;color:var(--muted)}
.btn{display:inline-block;border:2px solid var(--navy);color:var(--navy);font-size:13px;font-weight:600;padding:8px 22px;margin-top:30px}

/* departments */
.departments{height:460px;background:var(--navy);text-align:center;padding-top:50px}
.departments .section-title{color:var(--white)}
.departments .rule{background:var(--white)}
.dept-grid{display:flex;justify-content:center;gap:22px;margin-top:56px}
.dept-card{width:244px;height:220px;background:var(--white);position:relative;padding-top:82px}
.dept-photo{position:absolute;left:72px;top:-50px;width:100px;height:100px;border-radius:50%;border:4px solid var(--white);background:linear-gradient(135deg,#b9cce0,#e6edf4)}
.dept-card h3{font-size:15px;font-weight:600;color:var(--navy)}
.dept-card p{font-size:12px;line-height:1.6;color:var(--muted);margin:10px 28px 0}
.dept-card .btn-solid{display:inline-block;background:var(--navy);color:var(--white);font-size:12px;padding:6px 20px;margin-top:14px}

/* brochures */
.brochures{height:300px;position:relative;overflow:hidden;background:#eef2f7}
.brochure-photo{position:absolute;left:460px;top:0;right:0;bottom:0;background:linear-gradient(90deg,#e8dccf,#f5ece3 45%,#d8c3b4)}
.brochure-text{position:absolute;left:80px;top:110px;color:var(--white)}
.brochure-text h2{font-size:40px;font-weight:300}
.brochure-text p{font-size:20px;font-weight:300;margin-top:4px}
.slide-arrows{position:absolute;left:580px;top:232px;display:flex;gap:6px}

/* info */
.info{height:500px}
.info .wrap{display:flex;padding-top:40px}
.info-col{flex:1;padding:0 40px;min-height:300px}
.info-col + .info-col{border-left:1px solid var(--line)}
.info-col h2{font-size:26px;font-weight:400;color:var(--navy);text-align:center}
.info-col .rule{margin-bottom:26px}
.news-list{list-style:none}
.news-list li{font-size:12px;line-height:1.7;color:var(--muted);padding:10px 0 10px 18px;position:relative}
.news-list li::before{content:"";position:absolute;left:0;top:17px;width:6px;height:6px;background:var(--blue)}
.hours-lead{font-size:13px;color:var(--text);padding-left:18px;position:relative;margin-bottom:16px}
.hours-lead::before{content:"";position:absolute;left:0;top:6px;width:6px;height:6px;background:var(--blue)}
.hours dl{margin-left:110px;font-size:12px;line-height:1.6}
.hours dt{color:var(--navy);font-weight:600;margin-top:10px}
.hours dd{color:var(--muted)}

/* map */
.map{height:100px;background:linear-gradient(90deg,#e7ecd9,#efeee6 40%,#dde6ef 70%,#e5e9dc)}

/* footer */
.site-footer{height:72px;background:var(--footer);color:#c8d3ee;font-size:10px}
.site-footer .wrap{height:72px;display:flex;align-items:center;justify-content:space-between;white-space:nowrap}
.site-footer ul{list-style:none;display:flex;gap:10px}
</style>
</head>
<body>

<header class="site-header">
  <div class="wrap">
    <div class="brand">
      <span class="brand-mark"></span>
      <div>
        <div class="brand-name">The Corvane Pharmacy</div>
        <div class="brand-tag">"Caring Advice for Every Family"</div>
      </div>
    </div>
    <div class="contact">
      <div class="contact-row">
        <span class="contact-icon"><svg width="12" height="12" viewBox="0 0 24 24"><path fill="#fff" d="M6.6 10.8a15 15 0 0 0 6.6 6.6l2.2-2.2a1 1 0 0 1 1-.25 11.4 11.4 0 0 0 3.6.57 1 1 0 0 1 1 1V20a1 1 0 0 1-1 1A17 17 0 0 1 3 4a1 1 0 0 1 1-1h3.5a1 1 0 0 1 1 1c0 1.25.2 2.45.57 3.57a1 1 0 0 1-.25 1z"/></svg></span>
        +61 (07) 3000 4821
      </div>
      <div class="contact-row">
        <span class="contact-icon"><svg width="12" height="12" viewBox="0 0 24 24"><path fill="#fff" d="M2 5h20v14H2zm2 2v.5l8 5 8-5V7l-8 5z"/></svg></span>
        info@corvanepharmacy.com.au
      </div>
    </div>
  </div>
</header>

<nav class="main-nav">
  <ul>
    <li class="active">Home</li>
    <li>Community Pharmacy</li>
    <li>CPAP</li>
    <li>AMR</li>
    <li>Oncology services</li>
    <li>Home Nursing</li>
    <li>Nutrition</li>
    <li>Compounding</li>
    <li>Surgical Supply</li>
    <li>Contact Us</li>
  </ul>
</nav>

<section class="hero">
  <div class="hero-photo" role="img" aria-label="Photo of a smiling pharmacist in a white coat in a bright pharmacy"></div>
  <div class="hero-caption">
    <h1>Pharmaceutical <strong>COMPOUNDING</strong></h1>
    <p>The Corvane Pharmacy has an extensive range of medical equipment for hire and sale</p>
  </div>
  <div class="hero-dots"><span class="on"></span><span></span><span></span></div>
</section>

<section class="intro">
  <h2 class="section-title">Celebrating 38 Years of Service</h2>
  <div class="rule"></div>
  <p>Since March 1st 1977, The Corvane Pharmacy has been offering friendly service, professional advice and the solutions to any problem that a pharmacist can solve. We offer all of the things that you would expect from a regular Pharmacy as well as specialised services. We offer all of the things that you would expect from a regular Pharmacy as well as many more.</p>
  <span class="btn">Read More</span>
</section>

<section class="departments">
  <h2 class="section-title">Departments</h2>
  <div class="rule"></div>
  <div class="dept-grid">
    <article class="dept-card">
      <div class="dept-photo" role="img" aria-label="Photo of oncology care staff"></div>
      <h3>Oncology Service</h3>
      <p>Lorem Ipsum is simply dummy text of the printing and typesetting industry.</p>
      <span class="btn-solid">Read More</span>
    </article>
    <article class="dept-card">
      <div class="dept-photo" role="img" aria-label="Photo of a sleep apnoea mask"></div>
      <h3>Sleep Apnoea</h3>
      <p>Lorem Ipsum is simply dummy text of the printing and typesetting industry.</p>
      <span class="btn-solid">Read More</span>
    </article>
    <article class="dept-card">
      <div class="dept-photo" role="img" aria-label="Photo of pharmaceutical compounding work"></div>
      <h3>Pharmaceutical Compounding</h3>
      <p>Lorem Ipsum is simply dummy text of the printing and typesetting industry.</p>
      <span class="btn-solid">Read More</span>
    </article>
    <article class="dept-card">
      <div class="dept-photo" role="img" aria-label="Photo of a home nurse with a patient"></div>
      <h3>Home Nursing</h3>
      <p>Lorem Ipsum is simply dummy text of the printing and typesetting industry.</p>
      <span class="btn-solid">Read More</span>
    </article>
  </div>
</section>

<section class="brochures">
  <div class="brochure-photo" role="img" aria-label="Photo of a mother with her baby"></div>
  <svg width="620" height="300" style="position:absolute;left:0;top:0">
    <polygon points="0,0 460,0 560,150 460,300 0,300" fill="#3f6fcc"/>
    <polygon points="380,0 460,0 560,150 460,300 380,300 480,150" fill="#2a58b8"/>
  </svg>
  <div class="brochure-text">
    <h2>Brochures</h2>
    <p>Mother and Baby</p>
  </div>
  <div class="slide-arrows">
    <svg width="20" height="20" viewBox="0 0 20 20"><rect width="20" height="20" fill="#fff" opacity=".8"/><path d="M12 5l-5 5 5 5" stroke="#0d2f86" stroke-width="2" fill="none"/></svg>
    <svg width="20" height="20" viewBox="0 0 20 20"><rect width="20" height="20" fill="#fff" opacity=".8"/><path d="M8 5l5 5-5 5" stroke="#0d2f86" stroke-width="2" fill="none"/></svg>
  </div>
</section>

<section class="info">
  <div class="wrap">
    <div class="info-col">
      <h2>Health News</h2>
      <div class="rule"></div>
      <ul class="news-list">
        <li>Half of Australians now live with a chronic condition, a new national health report finds.</li>
        <li>Hospitals and local pharmacies team up to improve care for older patients.</li>
        <li>Doctors warn that seasonal flu cases are rising early this year across the region.</li>
      </ul>
    </div>
    <div class="info-col hours">
      <h2>Opening Hours</h2>
      <div class="rule"></div>
      <p class="hours-lead">We are open every day of the year</p>
      <dl>
        <dt>Monday to Friday</dt><dd>7:00am to 6:00pm</dd>
        <dt>Saturday</dt><dd>8:00am to 5:00pm</dd>
        <dt>Sunday and Public Holidays</dt><dd>8:00am to 1:00pm</dd>
      </dl>
    </div>
  </div>
</section>

<div class="map" role="img" aria-label="Street map showing the pharmacy location"></div>

<footer class="site-footer">
  <div class="wrap">
    <span>Copyright © 2014, All Rights Reserved by The Corvane Pharmacy</span>
    <ul>
      <li>Home</li><li>Community Pharmacy</li><li>CPAP</li><li>AMR</li><li>Oncology services</li><li>Home Nursing</li><li>Nutrition</li><li>Compounding</li><li>Surgical Supply</li><li>Contact Us</li>
    </ul>
  </div>
</footer>

</body>
</html>
```